New Architectural Firm Business Cards

New Business card to compliment previous pixel harbor logo (attached). Please design a business card that is simple, modern, creative....please do not use "symbols", simply the logo and associated graphics/text. The front should contain name/address/phone/email/web address (with graphics).....back should be 100% graphic design using the logo somehow. Hoping for a two color (black and yellow) design. full bleed design, no borders

Target Market(s)

Commercial Architecture Clients

Industry/Entity Type

Architecture

Contact Information for Business Card

Please design a business card that is simple, modern, creative....please do not use "symbols", simply the logo and associated graphics/text. The front should contain name/address/phone/email/web address (with graphics).....back should be 100% graphic design using the logo somehow

Font styles to use
Sans Serif

Colors
FFF300
FFF600
FEFA6F
FFFEC7
FFFEE8

Requirements
Must have
• Clean, Modern Design
Should not have
• Stock images or "icons"

```html
<!DOCTYPE html>
<html lang="en">
<head>
<meta charset="utf-8">
<title>pixel harbor business cards</title>
<link rel="stylesheet" href="https://fonts.googleapis.com/css2?family=Arimo:wght@400;700&display=swap">
<style>
  :root {
    --yellow: #f6c31a;
    --ink: #1e1e1e;
    --paper: #ffffff;
    --backdrop: #3a3a3a;
    --card-black: #121212;
    --pattern: #1f1f1f;
  }
  * { margin: 0; padding: 0; box-sizing: border-box; }
  html, body { width: 1200px; height: 801px; overflow: hidden; }
  body {
    background: var(--backdrop);
    font-family: "Arimo", Arial, sans-serif;
    position: relative;
  }
  .card {
    position: absolute;
    top: 252px;
    width: 520px;
    height: 297px;
    overflow: hidden;
  }
  .card-front { left: 60px; background: var(--paper); }
  .card-back { left: 620px; background: var(--card-black); }

  .front-band { position: absolute; inset: 0; width: 100%; height: 100%; }

  .brand-display {
    position: absolute;
    left: 268px;
    top: 58px;
    width: 240px;
    font-weight: 700;
    font-size: 50px;
    line-height: 0.95;
    color: var(--yellow);
    letter-spacing: -1px;
  }

  .contact { position: absolute; left: 34px; top: 120px; color: var(--ink); }
  .contact-name {
    font-weight: 700;
    font-size: 17px;
    letter-spacing: 0.5px;
    color: var(--yellow);
    text-transform: uppercase;
  }
  .contact-title { font-size: 11px; margin-top: 2px; }
  .divider {
    width: 12px; height: 2px;
    background: var(--yellow);
    margin: 9px 0 8px;
  }
  .contact-line { font-size: 10.5px; line-height: 1.45; }

  .back-pattern {
    position: absolute; inset: 0;
    background: linear-gradient(135deg, #242424 0%, var(--pattern) 55%, #0c0c0c 100%);
  }
  .back-brand {
    position: absolute;
    right: 26px;
    bottom: 28px;
    text-align: right;
  }
  .back-brand-name {
    font-weight: 700;
    font-size: 22px;
    line-height: 1;
    color: var(--yellow);
  }
  .back-brand-tag {
    font-size: 7.5px;
    letter-spacing: 0.8px;
    color: var(--paper);
    margin-top: 3px;
  }
</style>
</head>
<body>
  <section class="card card-front">
    <svg class="front-band" viewBox="0 0 520 297" aria-hidden="true">
      <polygon points="520,165 520,297 380,297 470,200" fill="var(--yellow)"/>
    </svg>
    <div class="brand-display">pixel harbor</div>
    <div class="contact">
      <div class="contact-name">Lena Marquez</div>
      <div class="contact-title">President</div>
      <div class="divider"></div>
      <div class="contact-line">P: 555 018 2040</div>
      <div class="contact-line">E: hello@pixelharbor.com</div>
      <div class="contact-line">www.pixelharbor.com</div>
      <div class="divider"></div>
      <div class="contact-line">18 Harbor Light Drive</div>
      <div class="contact-line">Suite 210, Westfield</div>
    </div>
  </section>

  <section class="card card-back">
    <div class="back-pattern" role="img" aria-label="Tone-on-tone black repeating brand pattern"></div>
    <div class="back-brand">
      <div class="back-brand-name">pixel harbor</div>
      <div class="back-brand-tag">ARCHITECTURE</div>
    </div>
  </section>
</body>
</html>
```